New Letterhead

Improve the attached letterhead to make it more alive and corporate class using the company colors in the two companies logos available on the two companies website.

Industry/Entity Type

Construction Company

Requirements
Must have
• colours of the two logod
Nice to have
• Be more alive and professional
Should not have
• Any other colours besides the ones in the logos

```html
<!DOCTYPE html>
<html lang="en">
<head>
<meta charset="utf-8">
<title>Kestrel Arden JV Letterhead</title>
<link href="https://fonts.googleapis.com/css2?family=Source+Sans+3:wght@400;600;700&family=Arimo:wght@700&display=swap" rel="stylesheet">
<style>
  :root {
    --teal: #2e96a3;
    --maroon: #8a2c1f;
    --ink: #2b2b2b;
    --body: #555555;
    --navy: #1a2450;
    --backdrop: #e6e6e6;
    --paper: #ffffff;
  }
  * { margin: 0; padding: 0; box-sizing: border-box; }
  html, body { width: 1200px; height: 1200px; overflow: hidden; background: var(--backdrop); }
  .letterhead {
    position: absolute; left: 189px; top: 20px;
    width: 822px; height: 1160px;
    background: var(--paper);
    font-family: "Source Sans 3", sans-serif;
    color: var(--body);
  }
  .edge-bar { position: absolute; left: 0; top: 0; width: 15px; height: 1160px; }
  .base-bar { position: absolute; left: 0; bottom: 0; width: 822px; height: 14px; }
  .brand {
    position: absolute; left: 62px; top: 52px;
    font-size: 44px; font-weight: 700; letter-spacing: 1px;
    color: var(--ink); line-height: 1;
  }
  .greeting {
    position: absolute; left: 66px; top: 245px;
    font-family: "Arimo", sans-serif; font-weight: 700;
    font-size: 19px; color: var(--navy);
  }
  .letter-body {
    position: absolute; left: 67px; top: 290px; width: 705px;
    font-size: 16.6px; line-height: 21.5px; text-align: justify;
  }
  .letter-body p + p { margin-top: 21.5px; }
  .signature {
    position: absolute; left: 68px; top: 700px;
    width: 153px; height: 76px;
    background: linear-gradient(135deg, #f2f2f2, #e4e4e4);
    border-radius: 4px;
  }
  .footer-col {
    position: absolute; top: 1070px;
    font-size: 11.6px; line-height: 16.5px; color: var(--ink);
  }
  .footer-col strong { font-weight: 700; }
  .col-primary { left: 61px; }
  .col-partner { left: 316px; padding-left: 0; }
  .col-registry { left: 592px; top: 1067px; }
  .divider { position: absolute; top: 1068px; width: 1px; height: 70px; background: #d0d0d0; }
  .contact-line { display: flex; align-items: center; gap: 4px; margin-top: 3px; }
  .contact-line svg { width: 10px; height: 10px; }
</style>
</head>
<body>
<main class="letterhead">
  <svg class="edge-bar" viewBox="0 0 15 1160" preserveAspectRatio="none">
    <polygon points="0,0 15,0 15,878 0,893" fill="var(--teal)"/>
    <polygon points="0,908 15,893 15,1160 0,1160" fill="var(--maroon)"/>
  </svg>
  <svg class="base-bar" viewBox="0 0 822 14" preserveAspectRatio="none">
    <defs>
      <linearGradient id="baseGrad" x1="0" x2="1" y1="0" y2="0">
        <stop offset="0" stop-color="#8a2c1f"/>
        <stop offset="1" stop-color="#2e96a3"/>
      </linearGradient>
    </defs>
    <rect width="822" height="14" fill="url(#baseGrad)"/>
  </svg>

  <div class="brand">KESTREL ARDEN</div>

  <h1 class="greeting">Dear Mr. Carter,</h1>

  <section class="letter-body">
    <p>Lorem Ipsum is simply dummy text of the printing and typesetting industry. Lorem Ipsum has been the industry's standard dummy text ever since the 1500s, when an unknown printer took a galley of type and scrambled it to make a type specimen book. It has survived not only five centuries, but also the leap into electronic typesetting, remaining essentially unchanged.</p>
    <p>The standard chunk of Lorem Ipsum used since the 1500s is reproduced below for those interested. Sections 1.10.32 and 1.10.33 from "de Finibus Bonorum et Malorum" by Cassian are also reproduced in their exact original form, accompanied by English versions from the 1914 translation by H. Rowell</p>
    <p>Lorem Ipsum is simply dummy text of the printing and typesetting industry. Lorem Ipsum has been the industry's standard dummy text ever since the 1500s, when an unknown printer took a galley of type and scrambled it to make a type specimen book. It has survived not only five centuries, but also the leap into electronic typesetting, remaining essentially unchanged. It was popularised in the</p>
  </section>

  <div class="signature" role="img" aria-label="Handwritten signature of the sender"></div>

  <footer>
    <div class="footer-col col-primary">
      <strong>Kestrel Arden JV (Pty) Limited</strong><br>
      12 Marlow Street Rosebank, Northvale<br>
      PO Box 55120, Hillcrest, 2031 South Africa
      <div class="contact-line">
        <svg viewBox="0 0 10 10"><path d="M2 1 L4 3 L3 4 Q4 6 6 7 L7 6 L9 8 L8 9 Q3 9 1 2 Z" fill="var(--ink)"/></svg>
        +27 (0)11 555 0142
        <svg viewBox="0 0 10 10"><circle cx="5" cy="5" r="4" fill="none" stroke="var(--ink)"/><path d="M1 5 H9 M5 1 V9" stroke="var(--ink)" stroke-width="0.8"/></svg>
        www.kestrelbuild.com
      </div>
    </div>
    <div class="divider" style="left:303px"></div>
    <div class="footer-col col-partner">
      <strong>Kestrel Arden JV (Pty) Limited</strong><br>
      27 Oakley Road, Cnr Baxter Avenue<br>
      Fairmead West, Northvale 2188 South Africa
      <div class="contact-line">
        <svg viewBox="0 0 10 10"><path d="M2 1 L4 3 L3 4 Q4 6 6 7 L7 6 L9 8 L8 9 Q3 9 1 2 Z" fill="var(--ink)"/></svg>
        +27 (0)11 555 0987
        <svg viewBox="0 0 10 10"><circle cx="5" cy="5" r="4" fill="none" stroke="var(--ink)"/><path d="M1 5 H9 M5 1 V9" stroke="var(--ink)" stroke-width="0.8"/></svg>
        www.ardenworks.com
      </div>
    </div>
    <div class="divider" style="left:579px"></div>
    <div class="footer-col col-registry">
      <strong>Registration No.:</strong> 2019/204417/07<br>
      Trading as Kestrel Arden JV (Pty) Limited<br>
      <strong>Directors:</strong><br>
      Peter Wells, Samuel Tandi Moreo
    </div>
  </footer>
</main>
</body>
</html>
```